" Empresa com inauguraçao prevista para Novembro 2018, voltada à atuaçao no segmento empresarial, com enfoque sobre soluçoes em tecnologia da informaçao. "

```html
<!DOCTYPE html>
<html lang="pt-BR">
<head>
<meta charset="UTF-8">
<title>Veranto Link – Pasta Interior</title>
<link href="https://fonts.googleapis.com/css2?family=Montserrat:wght@400;500&display=swap" rel="stylesheet">
<style>
  :root {
    --page-bg: #e9e7e3;
    --cover-deep: #18246a;
    --cover-mid: #2a3a94;
    --cover-shine: #4a5cb8;
    --inner-navy: #121b44;
    --inner-glow: #1b2a62;
    --pocket-navy: #17234f;
    --pocket-edge: #26346e;
    --text-light: #e8ecf8;
    --text-soft: #b9c3e6;
    --icon-bg: #3b4d9e;
    --slot-white: #ffffff;
  }
  * { margin: 0; padding: 0; box-sizing: border-box; }
  html, body {
    width: 1200px; height: 1200px; overflow: hidden;
    background: var(--page-bg);
    font-family: "Montserrat", Arial, sans-serif;
  }
  .folder-spread {
    position: absolute; left: 80px; top: 230px;
    width: 1040px; height: 740px;
    display: flex;
    box-shadow: 0 18px 40px rgba(0,0,0,0.18);
  }
  .panel { position: relative; width: 520px; height: 740px; overflow: hidden; }

  /* Left inside cover */
  .panel--cover {
    background: linear-gradient(100deg, var(--cover-deep) 0%, var(--cover-mid) 35%, var(--cover-shine) 52%, var(--cover-mid) 68%, var(--cover-deep) 100%);
  }
  .brand {
    position: absolute; left: 0; right: 0;
    display: flex; flex-direction: column; align-items: center; gap: 14px;
  }
  .panel--cover .brand { top: 300px; }
  .brand__mark {
    width: 62px; height: 62px; border-radius: 50%;
    border: 3px solid var(--text-light);
  }
  .brand__name {
    color: var(--text-light); font-weight: 500;
    font-size: 30px; letter-spacing: 1px; text-transform: uppercase;
    white-space: nowrap;
  }

  /* Right inside panel with pocket */
  .panel--pocket {
    background: radial-gradient(circle at 80% 15%, var(--inner-glow) 0%, var(--inner-navy) 55%);
  }
  .pocket {
    position: absolute; left: 0; right: 0; top: 190px; bottom: 0;
    background: var(--pocket-navy);
    border-top: 2px solid var(--pocket-edge);
  }
  .card-slot {
    position: absolute; left: -110px; top: 80px;
    width: 220px; height: 380px; border-radius: 50%;
    background: var(--slot-white);
  }
  .pocket .brand { top: 130px; padding-left: 110px; }
  .pocket .brand__mark { width: 50px; height: 50px; }
  .pocket .brand__name { font-size: 25px; }

  .contact-list {
    position: absolute; left: 110px; right: 30px; top: 260px;
    display: grid; grid-template-columns: 1fr 1.1fr; gap: 14px 20px;
    list-style: none;
  }
  .contact-item {
    display: flex; align-items: flex-start; gap: 8px;
    color: var(--text-soft); font-size: 10.5px; line-height: 1.4;
    white-space: nowrap;
  }
  .contact-item svg { flex: none; width: 16px; height: 16px; }
</style>
</head>
<body>
  <main class="folder-spread">
    <section class="panel panel--cover">
      <div class="brand">
        <span class="brand__mark"></span>
        <span class="brand__name">Veranto Link</span>
      </div>
    </section>

    <section class="panel panel--pocket">
      <div class="pocket">
        <div class="brand">
          <span class="brand__mark"></span>
          <span class="brand__name">Veranto Link</span>
        </div>
        <ul class="contact-list">
          <li class="contact-item">
            <svg viewBox="0 0 16 16"><circle cx="8" cy="8" r="8" fill="#3b4d9e"/><path d="M5.2 4.5l1.4-.3.8 1.8-.9.7a5 5 0 0 0 2.8 2.8l.7-.9 1.8.8-.3 1.4c-3.5.3-6.6-2.8-6.3-6.3z" fill="#e8ecf8"/></svg>
            <span>(11) 4000-2018<br>(11) 98000-2018</span>
          </li>
          <li class="contact-item">
            <svg viewBox="0 0 16 16"><circle cx="8" cy="8" r="8" fill="#3b4d9e"/><path d="M8 3.5a2.8 2.8 0 0 0-2.8 2.8C5.2 8.5 8 12 8 12s2.8-3.5 2.8-5.7A2.8 2.8 0 0 0 8 3.5zm0 3.9a1.1 1.1 0 1 1 0-2.2 1.1 1.1 0 0 1 0 2.2z" fill="#e8ecf8"/></svg>
            <span>Rua das Acácias, 120<br>Centro, São Paulo - SP</span>
          </li>
          <li class="contact-item">
            <svg viewBox="0 0 16 16"><circle cx="8" cy="8" r="8" fill="#3b4d9e"/><circle cx="8" cy="8" r="3.6" fill="none" stroke="#e8ecf8" stroke-width="1"/><path d="M4.4 8h7.2M8 4.4c1.5 1.8 1.5 5.4 0 7.2M8 4.4c-1.5 1.8-1.5 5.4 0 7.2" stroke="#e8ecf8" stroke-width=".8" fill="none"/></svg>
            <span>www.verantolink.com.br</span>
          </li>
          <li class="contact-item">
            <svg viewBox="0 0 16 16"><circle cx="8" cy="8" r="8" fill="#3b4d9e"/><rect x="4" y="5.2" width="8" height="5.6" rx=".6" fill="none" stroke="#e8ecf8" stroke-width="1"/><path d="M4.3 5.6L8 8.4l3.7-2.8" fill="none" stroke="#e8ecf8" stroke-width="1"/></svg>
            <span>contato@verantolink.com.br</span>
          </li>
        </ul>
      </div>
      <div class="card-slot"></div>
    </section>
  </main>
</body>
</html>
```